Business Card for TKR, logo files already created

Please, can you assist with creating a Business card the TKR graphics which are already listed on www.tarnkeyrelay.example
The business card should be modern and upmarket, textured designs are welcome. Please feel free to express yourself and be very bold with your design.

Target Market(s)

Cyber Security

Industry/Entity Type

Information Technology

Contact Information for Business Card

Company Name
Name
Title
Mobile
Fax or Tel
email
url

Font styles to use
Serif
Sans Serif

Colors
3277b5
85acd3
ffffff

```html
<!DOCTYPE html>
<html lang="en">
<head>
<meta charset="utf-8">
<title>TKR Business Card</title>
<link href="https://fonts.googleapis.com/css2?family=Maven+Pro:wght@400;500;700;900&display=swap" rel="stylesheet">
<style>
  :root {
    --backdrop: #3b3b3d;
    --card: #252426;
    --card-emboss: #111112;
    --brand-blue: #3277b5;
    --brand-light: #85acd3;
    --white: #ffffff;
    --muted: #e6e6e6;
  }
  * { margin: 0; padding: 0; box-sizing: border-box; }
  html, body {
    width: 1200px; height: 900px; overflow: hidden;
    background: var(--backdrop);
    font-family: "Maven Pro", sans-serif;
  }
  .stage {
    width: 1200px; height: 900px;
    display: flex; flex-direction: column;
    align-items: center; justify-content: center; gap: 36px;
  }
  .card {
    width: 700px; height: 400px;
    background: var(--card);
    position: relative;
    box-shadow: 0 12px 30px rgba(0,0,0,0.45);
  }
  /* Front */
  .card-front { display: flex; align-items: center; justify-content: center; }
  .front-mark {
    display: flex; align-items: center; gap: 22px;
    color: var(--card-emboss);
    font-weight: 900; font-size: 130px; letter-spacing: 4px; line-height: 1;
  }
  .front-mark .mark-square { width: 52px; height: 52px; background: var(--card-emboss); }

  /* Back */
  .brand-lockup {
    position: absolute; left: 60px; top: 118px;
    display: flex; align-items: center; gap: 16px;
    color: var(--brand-blue);
    font-weight: 900; font-size: 92px; letter-spacing: 3px; line-height: 1;
  }
  .brand-lockup .mark-square { width: 34px; height: 34px; background: var(--brand-blue); }
  .contact {
    position: absolute; left: 378px; top: 100px;
    color: var(--white);
  }
  .contact-name { color: var(--brand-blue); font-size: 28px; font-weight: 500; letter-spacing: 0.5px; }
  .contact-title { font-size: 15px; margin-top: 2px; color: var(--muted); }
  .contact-list { list-style: none; margin-top: 26px; }
  .contact-list li {
    display: flex; align-items: center; gap: 14px;
    font-size: 18px; letter-spacing: 0.4px; height: 30px;
  }
  .contact-list svg { width: 20px; height: 20px; fill: var(--brand-blue); flex: none; }
  .website {
    position: absolute; left: 0; right: 0; bottom: 46px;
    text-align: center; color: var(--white); font-size: 20px; letter-spacing: 0.4px;
  }
  .website .domain { color: var(--brand-blue); }
</style>
</head>
<body>
<main class="stage">
  <section class="card card-front" aria-label="Card front">
    <div class="front-mark"><span class="mark-square"></span>TKR</div>
  </section>

  <section class="card card-back" aria-label="Card back">
    <div class="brand-lockup"><span class="mark-square"></span>TKR</div>

    <div class="contact">
      <p class="contact-name">Daniel Reyes</p>
      <p class="contact-title">Founder</p>
      <ul class="contact-list">
        <li>
          <svg viewBox="0 0 24 24" aria-hidden="true"><path d="M6.6 10.8a15.1 15.1 0 0 0 6.6 6.6l2.2-2.2a1 1 0 0 1 1-.25 11.4 11.4 0 0 0 3.6.57 1 1 0 0 1 1 1V20a1 1 0 0 1-1 1A17 17 0 0 1 3 4a1 1 0 0 1 1-1h3.5a1 1 0 0 1 1 1c0 1.25.2 2.45.57 3.57a1 1 0 0 1-.25 1z"/></svg>
          <span>800 - 555 - 0146</span>
        </li>
        <li>
          <svg viewBox="0 0 24 24" aria-hidden="true"><path d="M7 2h8l3 3v5H7z M3 10h18a1 1 0 0 1 1 1v10a1 1 0 0 1-1 1H3a1 1 0 0 1-1-1V11a1 1 0 0 1 1-1zm3 3v2h2v-2zm4 0v2h2v-2zm4 0v2h4v-2zm-8 4v2h2v-2zm4 0v2h2v-2z"/></svg>
          <span>800 - 555 - 0155</span>
        </li>
        <li>
          <svg viewBox="0 0 24 24" aria-hidden="true"><path d="M2 5h20v2l-10 6L2 7z M2 9.3l10 6 10-6V19H2z"/></svg>
          <span>contact@tarnkeyrelay.example</span>
        </li>
      </ul>
    </div>

    <p class="website">www.<span class="domain">tarnkeyrelay</span>.example</p>
  </section>
</main>
</body>
</html>
```